indépendant en tant que Massothérapeute et Préparateur Mental, j'ai besoin de ...

Massothérapeute et préparateur mental indépendant, je recherche une carte de visite sobre et dynamique, sans images liées au massage ou à la préparation mentale mais intégrant mon logo. Les couleurs que j'aime bien sont : Blanc, gris, anthracite, noir et jaune

Contact Information for Business Card

carte de préférence Horizontale
neutre qui puisse toucher le deux domaines Massothérapie et préparation mentale

Requirements
Must have
• mon projet doit intégrer au recto:
LOGO
Loïc Vermande
078 315 26 49
info@loicvermande-exemple.ch
et éventuellement www.loicvermande-exemple.ch

et au verso les deux adresses:

Chemin des Ormelets 27B
1400 Yverdon-les-Bains

Rue des Tanneries 9
1700 Fribourg

Should not have
• mon projet ne doit pas contenir d'image en liens avec le massage ni la préparation mentale.

```html
<!DOCTYPE html>
<html lang="fr">
<head>
<meta charset="utf-8">
<title>Loïc Vermande – Carte de visite</title>
<link rel="stylesheet" href="https://fonts.googleapis.com/css2?family=Roboto:wght@300;400&display=swap">
<style>
  :root {
    --backdrop: #ecebe9;
    --card: #1f2833;
    --ink: #f2f2f2;
    --ink-soft: #c9ccd1;
    --accent: #e8b021;
    --rule: #6d737c;
  }
  * { box-sizing: border-box; margin: 0; padding: 0; }
  html, body { width: 1200px; height: 960px; overflow: hidden; }
  body {
    background: var(--backdrop);
    font-family: "Roboto", Arial, sans-serif;
    color: var(--ink);
    position: relative;
  }
  .card {
    position: absolute;
    left: 280px;
    width: 640px;
    height: 414px;
    background: var(--card);
    border-radius: 4px;
    box-shadow: 0 6px 18px rgba(0,0,0,.12);
  }
  .card--front { top: 36px; }
  .card--back { top: 506px; }

  .brand__name {
    font-weight: 300;
    color: var(--ink);
    letter-spacing: .5px;
    white-space: nowrap;
  }
  .brand__role {
    font-weight: 300;
    color: var(--ink-soft);
    text-transform: uppercase;
    letter-spacing: 1.2px;
    white-space: nowrap;
    margin-top: 8px;
  }

  /* recto */
  .card--front .brand { position: absolute; left: 56px; top: 178px; }
  .card--front .brand__name { font-size: 28px; }
  .card--front .brand__role { font-size: 8.5px; }
  .divider {
    position: absolute; left: 322px; top: 140px;
    width: 1px; height: 134px; background: var(--rule);
  }
  .contact-list {
    position: absolute; left: 342px; top: 157px;
    list-style: none;
  }
  .contact-list li {
    display: flex; align-items: center; gap: 9px;
    font-size: 15px; font-weight: 400; color: var(--ink);
    height: 34px; white-space: nowrap;
  }
  .icon {
    width: 20px; height: 20px; border-radius: 50%;
    background: var(--accent);
    display: flex; align-items: center; justify-content: center;
    flex: none;
  }
  .icon svg { width: 12px; height: 12px; }

  /* verso */
  .card--back .brand { position: absolute; left: 70px; top: 130px; }
  .card--back .brand__name { font-size: 44px; }
  .card--back .brand__role { font-size: 11px; margin-top: 10px; }
  .address {
    position: absolute;
    display: flex; gap: 9px; align-items: flex-start;
    font-size: 15px; line-height: 1.3; color: var(--ink);
    font-style: normal;
  }
  .address .icon { margin-top: 1px; }
  .address--yverdon { left: 56px; top: 318px; }
  .address--fribourg { left: 402px; top: 70px; }
</style>
</head>
<body>

<section class="card card--front" aria-label="Recto">
  <div class="brand">
    <p class="brand__name">Loïc Vermande</p>
    <p class="brand__role">… Massothérapeute / Préparateur mental …</p>
  </div>
  <div class="divider"></div>
  <ul class="contact-list">
    <li>
      <span class="icon"><svg viewBox="0 0 24 24"><path fill="#1f2833" d="M6.6 10.8a15 15 0 0 0 6.6 6.6l2.2-2.2c.3-.3.7-.4 1-.2 1.1.4 2.3.6 3.6.6.6 0 1 .4 1 1V20c0 .6-.4 1-1 1A17 17 0 0 1 3 4c0-.6.4-1 1-1h3.5c.6 0 1 .4 1 1 0 1.2.2 2.4.6 3.6.1.3 0 .7-.2 1z"/></svg></span>
      078 315 26 49
    </li>
    <li>
      <span class="icon"><svg viewBox="0 0 24 24"><rect x="3" y="5" width="18" height="14" rx="2" fill="none" stroke="#1f2833" stroke-width="2.4"/><path d="M3.5 6l8.5 7 8.5-7" fill="none" stroke="#1f2833" stroke-width="2.4"/></svg></span>
      info@loicvermande-exemple.ch
    </li>
    <li>
      <span class="icon"><svg viewBox="0 0 24 24"><circle cx="12" cy="12" r="9" fill="none" stroke="#1f2833" stroke-width="2.2"/><ellipse cx="12" cy="12" rx="4" ry="9" fill="none" stroke="#1f2833" stroke-width="2"/><path d="M3 12h18" stroke="#1f2833" stroke-width="2"/></svg></span>
      www.loicvermande-exemple.ch
    </li>
  </ul>
</section>

<section class="card card--back" aria-label="Verso">
  <div class="brand">
    <p class="brand__name">Loïc Vermande</p>
    <p class="brand__role">… Massothérapeute / Préparateur mental …</p>
  </div>
  <address class="address address--fribourg">
    <span class="icon"><svg viewBox="0 0 24 24"><path fill="#1f2833" d="M12 2a7 7 0 0 0-7 7c0 5 7 13 7 13s7-8 7-13a7 7 0 0 0-7-7zm0 9.5A2.5 2.5 0 1 1 12 6.5a2.5 2.5 0 0 1 0 5z"/></svg></span>
    <span>Rue des Tanneries 9<br>1700 Fribourg</span>
  </address>
  <address class="address address--yverdon">
    <span class="icon"><svg viewBox="0 0 24 24"><path fill="#1f2833" d="M12 2a7 7 0 0 0-7 7c0 5 7 13 7 13s7-8 7-13a7 7 0 0 0-7-7zm0 9.5A2.5 2.5 0 1 1 12 6.5a2.5 2.5 0 0 1 0 5z"/></svg></span>
    <span>Chemin des Ormelets 27B<br>1400 Yverdon-les-Bains</span>
  </address>
</section>

</body>
</html>
```